VeltaFilez Website

VeltaFiles - Organized Medical Docz
We need a Web design for a new company called - VeltaFilez.
VeltaFilez is a Personal Injury and Medical Record Legal Service Outsourcing company. We help Personal Injury Attorneys - with fact based Medical Chronologies and Summaries.

We take Medical Records in disarray and put them in order and summarize them in a chronological order and Update them as needed (if more medical records are added)
Take Releases (for medical records) and work with doctor practices and get the records if needed

Target Market(s)

Personal Injury Attorneys

Industry/Entity Type

Attorney

Number of Pages Required

2 page

Font styles to use
Serif
Sans Serif

Colors

Designer to choose colors to be used in the design.

Requirements
Must have
• Professional Design
• Just need the design for the Home page and Internal pages - I will do the Coding for the pages in html and/or wordpress.
• Don't worry about the content - just need a design.

```html
<!DOCTYPE html>
<html lang="en">
<head>
<meta charset="utf-8">
<title>VeltaFilez – Organized Medical Records</title>
<link href="https://fonts.googleapis.com/css2?family=Open+Sans:wght@300;400;600;700&display=swap" rel="stylesheet">
<style>
:root{
  --navy:#1a3f74;
  --ink:#0e1a3a;
  --text:#222;
  --muted:#444;
  --band-grey:#ebebeb;
  --band-contact:#0b3150;
  --footer:#000;
  --white:#fff;
  --ring:#dcdcdc;
  --icon:#4a4a4a;
}
*{margin:0;padding:0;box-sizing:border-box}
html,body{width:1200px;height:2659px;overflow:hidden}
body{position:relative;background:var(--white);font-family:"Open Sans",Arial,sans-serif;color:var(--text)}
.abs{position:absolute}
.center{left:0;width:1200px;text-align:center}

/* header */
.site-header{position:absolute;left:0;top:0;width:1200px;height:105px;background:var(--white)}
.brand{position:absolute;left:46px;top:30px;display:flex;align-items:center;gap:12px}
.brand-mark{width:34px;height:34px;background:var(--navy)}
.brand-name{font-size:30px;font-weight:600;color:var(--navy);letter-spacing:.5px}
.nav{position:absolute;top:40px;left:502px;height:36px;width:510px}
.nav a{font-size:17px;font-weight:600;color:#555;text-decoration:none;position:absolute;top:0;white-space:nowrap;line-height:36px}
.nav .active{background:var(--navy);color:var(--white);width:83px;text-align:center;left:0}
.nav-phone{position:absolute;left:1026px;top:40px;height:36px;display:flex;align-items:center;gap:7px;font-size:17px;font-weight:700;color:var(--ink)}

/* hero */
.hero{position:absolute;left:0;top:105px;width:1200px;height:562px;
  background:linear-gradient(120deg,#2a3056 0%,#3b4168 40%,#6d7292 70%,#3a3f66 100%)}
.hero-title{position:absolute;left:46px;top:236px;font-size:48px;font-weight:700;color:var(--white)}
.hero-text{position:absolute;left:46px;top:326px;width:760px;font-size:23px;line-height:30px;color:var(--white)}
.btn{position:absolute;height:55px;line-height:53px;text-align:center;font-size:23px;color:var(--white)}
.btn-outline{left:48px;top:418px;width:186px;border:2px solid var(--white)}
.btn-solid{left:255px;top:418px;width:186px;background:var(--navy)}

/* section headings */
.section-title{font-size:35px;font-weight:700;color:var(--ink)}
.section-title span{color:var(--navy)}
.section-sub{font-size:20px;font-weight:400;color:var(--muted)}

/* services */
.service{position:absolute;width:360px;text-align:center}
.service-ring{width:164px;height:164px;margin:0 auto;border:3px solid var(--ring);border-radius:50%;display:flex;align-items:center;justify-content:center}
.service-name{margin-top:8px;font-size:22px;font-weight:700;color:var(--navy)}
.service-text{margin-top:6px;font-size:17.5px;line-height:25.5px;color:var(--text)}

/* about */
.about{position:absolute;left:0;top:1269px;width:1200px;height:314px;background:var(--band-grey)}
.about-text{position:absolute;left:60px;top:1405px;width:1080px;text-align:center;font-size:16px;line-height:25.5px;color:var(--text)}

/* testimonials */
.testimonial{position:absolute;width:370px;text-align:center}
.avatar{width:92px;height:92px;margin:0 auto;border-radius:50%;border:3px solid #bfbfbf;background:radial-gradient(circle at 50% 40%,#7d8d8a,#34484a)}
.testimonial-name{margin-top:10px;font-size:16px;font-weight:700;color:var(--ink)}
.testimonial-text{margin-top:6px;font-size:17.5px;line-height:25px;color:var(--text)}

/* contact band */
.contact-band{position:absolute;left:0;top:2116px;width:1200px;height:188px;background:var(--band-contact)}
.contact-band .section-title{color:var(--white)}
.contact-band .section-sub{color:var(--white)}
.btn-touch{left:484px;top:2228px;width:232px;border:2px solid #cfd8e0;height:55px;line-height:51px;font-weight:300}

/* footer */
.site-footer{position:absolute;left:0;top:2304px;width:1200px;height:355px;background:var(--footer);color:var(--white)}
.footer-col{position:absolute;top:66px}
.footer-col h4{font-size:21px;font-weight:600;margin-bottom:14px}
.footer-col li{list-style:none;font-size:17px;font-weight:300;line-height:25.5px}
.footer-contact li{display:flex;gap:8px;align-items:flex-start;margin-bottom:8px}
.footer-contact svg{flex:none;margin-top:5px}
.social li{line-height:31px}
.copyright{position:absolute;left:0;top:2618px;width:1200px;text-align:center;font-size:14px;color:#333}
</style>
</head>
<body>

<header class="site-header">
  <div class="brand"><div class="brand-mark"></div><div class="brand-name">VeltaFilez</div></div>
  <nav class="nav">
    <a class="active">Home</a>
    <a style="left:102px">About</a>
    <a style="left:188px">Services</a>
    <a style="left:292px">Case Studies</a>
    <a style="left:432px">Contact</a>
  </nav>
  <div class="nav-phone">
    <svg width="20" height="22" viewBox="0 0 20 22"><rect x="3" y="1" width="13" height="20" rx="3" fill="var(--navy)"/><rect x="6" y="4" width="7" height="12" fill="#fff"/></svg>
    1800-555-01
  </div>
</header>

<section class="hero" role="img" aria-label="Photo of a tall library with curved bookshelves under a skylight, dark blue tint"></section>
<h1 class="hero-title">Pellentesque Cursus Justo</h1>
<p class="hero-text">Suspendisse pellentesque eu mi vel hendrerit. In hac habitasse platea dictumst. Cras a lorem in metus vulputate ultricies et in tellus.</p>
<div class="btn btn-outline">Learn More</div>
<div class="btn btn-solid">Contact Us</div>

<h2 class="abs center section-title" style="top:748px">Our <span>Services</span></h2>
<p class="abs center section-sub" style="top:798px">Vestibulum quam diam hendrerit vel viverra sit amet fringilla et diam.</p>

<div class="service" style="left:33px;top:868px">
  <div class="service-ring"><svg width="86" height="86" viewBox="0 0 86 86"><g fill="var(--icon)"><circle cx="43" cy="43" r="28"/><rect x="37" y="5" width="12" height="76"/><rect x="5" y="37" width="76" height="12"/><rect x="37" y="5" width="12" height="76" transform="rotate(45 43 43)"/><rect x="37" y="5" width="12" height="76" transform="rotate(-45 43 43)"/></g><circle cx="43" cy="43" r="17" fill="#fff"/><rect x="39" y="26" width="8" height="34" fill="var(--icon)" transform="rotate(45 43 43)"/></svg></div>
  <div class="service-name">Praesent</div>
  <p class="service-text">Lorem ipsum dolor sit amet, consectetur adipiscing elit. Curabitur dui nulla, ac malesuada ac tortor. Aenean sit amet felis non nunc tempor dignissim quis sed urna.</p>
</div>
<div class="service" style="left:419px;top:868px">
  <div class="service-ring"><svg width="86" height="86" viewBox="0 0 86 86"><g fill="var(--icon)"><circle cx="43" cy="43" r="28"/><rect x="37" y="5" width="12" height="76"/><rect x="5" y="37" width="76" height="12"/><rect x="37" y="5" width="12" height="76" transform="rotate(45 43 43)"/><rect x="37" y="5" width="12" height="76" transform="rotate(-45 43 43)"/></g><circle cx="43" cy="43" r="17" fill="#fff"/><rect x="39" y="26" width="8" height="34" fill="var(--icon)" transform="rotate(45 43 43)"/></svg></div>
  <div class="service-name">Praesent</div>
  <p class="service-text">Lorem ipsum dolor sit amet, consectetur adipiscing elit. Curabitur dui nulla, ac malesuada ac tortor. Aenean sit amet felis non nunc tempor dignissim quis sed urna.</p>
</div>
<div class="service" style="left:805px;top:868px">
  <div class="service-ring"><svg width="86" height="86" viewBox="0 0 86 86"><g fill="var(--icon)"><circle cx="43" cy="43" r="28"/><rect x="37" y="5" width="12" height="76"/><rect x="5" y="37" width="76" height="12"/><rect x="37" y="5" width="12" height="76" transform="rotate(45 43 43)"/><rect x="37" y="5" width="12" height="76" transform="rotate(-45 43 43)"/></g><circle cx="43" cy="43" r="17" fill="#fff"/><rect x="39" y="26" width="8" height="34" fill="var(--icon)" transform="rotate(45 43 43)"/></svg></div>
  <div class="service-name">Praesent</div>
  <p class="service-text">Lorem ipsum dolor sit amet, consectetur adipiscing elit. Curabitur dui nulla, ac malesuada ac tortor. Aenean sit amet felis non nunc tempor dignissim quis sed urna.</p>
</div>

<section class="about"></section>
<h2 class="abs center section-title" style="top:1287px">About <span>Us</span></h2>
<p class="abs center section-sub" style="top:1335px">Vestibulum quam diam hendrerit vel viverra sit amet fringilla et diam.</p>
<p class="about-text">Lorem ipsum dolor sit amet, consectetur adipiscing elit. Curabitur dui nulla, condimentum ac facilisis ac, malesuada ac tortor. Aenean sit amet felis non nunc tempor dignissim quis sed urna. Nunc sed venenatis diam, eu suscipit nunc. Curabitur ullamcorper purus id sapien venenatis, vel vestibulum erat molestie. Vestibulum a lorem sed sapien condimentum vulputate. Duis fermentum, ipsum a aliquet venenatis, mauris mauris sagittis mi, accumsan elementum ipsum lorem ac tellus.</p>

<h2 class="abs center section-title" style="top:1668px"><span>Testimonials</span></h2>
<p class="abs center section-sub" style="top:1716px">Vestibulum quam diam hendrerit vel viverra sit amet fringilla et diam.</p>

<div class="testimonial" style="left:28px;top:1799px">
  <div class="avatar" role="img" aria-label="Portrait photo of the client"></div>
  <div class="testimonial-name">Martin K. Ellery</div>
  <p class="testimonial-text">Duis fermentum, ipsum a aliquet venenatis, mauris mauris sagittis mi, accumsan elementum ipsum lorem ac tellus.</p>
</div>
<div class="testimonial" style="left:415px;top:1799px">
  <div class="avatar" role="img" aria-label="Portrait photo of the client"></div>
  <div class="testimonial-name">Martin K. Ellery</div>
  <p class="testimonial-text">Duis fermentum, ipsum a aliquet venenatis, mauris mauris sagittis mi, accumsan elementum ipsum lorem ac tellus.</p>
</div>
<div class="testimonial" style="left:801px;top:1799px">
  <div class="avatar" role="img" aria-label="Portrait photo of the client"></div>
  <div class="testimonial-name">Martin K. Ellery</div>
  <p class="testimonial-text">Duis fermentum, ipsum a aliquet venenatis, mauris mauris sagittis mi, accumsan elementum ipsum lorem ac tellus.</p>
</div>

<section class="contact-band">
  <h2 class="abs center section-title" style="top:6px">Contact Us</h2>
  <p class="abs center section-sub" style="top:54px">Vestibulum quam diam hendrerit vel viverra sit amet fringilla et diam.</p>
</section>
<div class="btn btn-touch">Get in touch</div>

<footer class="site-footer">
  <div class="footer-col" style="left:46px">
    <h4>Quick Links</h4>
    <ul><li>Home</li><li>About</li><li>Services</li><li>Case Studies</li><li>Contact Us</li></ul>
  </div>
  <div class="footer-col" style="left:378px">
    <h4>Services</h4>
    <ul><li>Sedarcu</li><li>Justo</li><li>Semper</li><li>Sitamet</li><li>Feugiat</li></ul>
  </div>
  <div class="footer-col footer-contact" style="left:637px">
    <h4 style="margin-left:24px">Contact</h4>
    <ul>
      <li><svg width="14" height="18" viewBox="0 0 14 18"><path d="M7 0a7 7 0 0 0-7 7c0 5 7 11 7 11s7-6 7-11a7 7 0 0 0-7-7z" fill="#fff"/><circle cx="7" cy="7" r="2.6" fill="#000"/></svg><span>417 Harbor Mill Road<br>Fernbrook, FL 30127</span></li>
      <li><svg width="14" height="14" viewBox="0 0 14 14"><path d="M3 0l3 3-2 2c1 2 3 4 5 5l2-2 3 3-2 3C6 13 1 8 0 3z" fill="#fff"/></svg><span>1800-555-01</span></li>
      <li><svg width="16" height="12" viewBox="0 0 16 12"><rect width="16" height="12" fill="#fff"/><path d="M0 0l8 7 8-7" fill="none" stroke="#000" stroke-width="1.5"/></svg><span>mail@veltafilez.com</span></li>
    </ul>
  </div>
  <div class="footer-col social" style="left:984px">
    <h4>Connect with us</h4>
    <ul><li>Friendloop</li><li>Chirpline</li><li>Snapgrid</li><li>Workweb</li></ul>
  </div>
</footer>
<p class="copyright">Copyright © 2018 VeltaFilez | Privacy | Sitemap</p>

</body>
</html>
```